Tirovel

We need a business card for our company is a holding for different business all are different we try to have some air of relax and fun in our projects we add pictures of the office to give you an idea od the mood of the business

Business

```html
<!DOCTYPE html>
<html lang="en">
<head>
<meta charset="utf-8">
<title>Tirovel – Business Card</title>
<link rel="stylesheet" href="https://fonts.googleapis.com/css2?family=Arimo:wght@400;700&display=swap">
<style>
  :root {
    --backdrop: #e9e6e1;
    --card-black: #111111;
    --brand-yellow: #f5e000;
    --text-font: "Arimo", Arial, sans-serif;
  }
  html, body {
    margin: 0;
    padding: 0;
    width: 1200px;
    height: 974px;
    overflow: hidden;
    background: var(--backdrop);
  }
  .canvas {
    position: relative;
    width: 1200px;
    height: 974px;
  }
  .business-card {
    position: absolute;
    left: 100px;
    top: 201px;
    width: 1000px;
    height: 572px;
    background: var(--card-black);
    overflow: hidden;
    font-family: var(--text-font);
    box-shadow: 0 10px 30px rgba(0,0,0,0.18);
  }
  .brand {
    position: absolute;
    left: 80px;
    top: 192px;
    display: flex;
    align-items: center;
    gap: 18px;
  }
  .brand-mark {
    width: 58px;
    height: 58px;
    background: var(--brand-yellow);
    flex: none;
  }
  .brand-name {
    margin: 0;
    font-family: var(--text-font);
    font-weight: 700;
    font-size: 64px;
    line-height: 1;
    color: var(--brand-yellow);
  }
  .contact-frame {
    position: absolute;
    left: 480px;
    top: 300px;
    width: 560px;
    height: 176px;
    border: 7px solid var(--brand-yellow);
    border-right: none;
    border-radius: 95px 0 0 95px;
    box-sizing: border-box;
  }
  .contact-details {
    position: absolute;
    left: 560px;
    top: 328px;
    margin: 0;
    font-style: normal;
    color: var(--brand-yellow);
  }
  .contact-name {
    margin: 0 0 10px;
    font-size: 30px;
    font-weight: 700;
  }
  .contact-line {
    display: flex;
    align-items: center;
    gap: 12px;
    margin: 0 0 8px;
    font-size: 27px;
    font-weight: 400;
  }
  .contact-icon {
    width: 24px;
    height: 24px;
    flex: none;
  }
</style>
</head>
<body>
  <main class="canvas">
    <article class="business-card">
      <div class="brand">
        <span class="brand-mark" aria-hidden="true"></span>
        <p class="brand-name">Tirovel</p>
      </div>

      <div class="contact-frame"></div>

      <address class="contact-details">
        <p class="contact-name">Name Here</p>
        <p class="contact-line">
          <svg class="contact-icon" viewBox="0 0 24 24" aria-hidden="true">
            <circle cx="12" cy="12" r="12" fill="var(--brand-yellow)"/>
            <path d="M8.5 6.5l2 2.2-1.2 1.6c.8 1.7 2 2.9 3.6 3.7l1.6-1.2 2.2 2-1.3 1.8c-4.2-.6-8-4.4-8.6-8.6z" fill="var(--card-black)"/>
          </svg>
          +00 585 8888 99
        </p>
        <p class="contact-line">
          <svg class="contact-icon" viewBox="0 0 24 24" aria-hidden="true">
            <circle cx="12" cy="12" r="12" fill="var(--brand-yellow)"/>
            <rect x="5.5" y="8" width="13" height="9" fill="none" stroke="var(--card-black)" stroke-width="1.6"/>
            <path d="M5.5 8l6.5 5 6.5-5" fill="none" stroke="var(--card-black)" stroke-width="1.6"/>
          </svg>
          xxxx@xxxxxxx.com
        </p>
      </address>
    </article>
  </main>
</body>
</html>
```